Business Card Design Project

Need a business card with logo that is attached.
Company name: Moberly Swift Solutions, LLC
My name: Lucia Pembrook
Title: President
Phone number: 703-482-1947
Email: lpembrook@moberlyswiftsolutions.example
web site: www.moberlyswiftsolutions.example

Industry/Entity Type

Business

```html
<!DOCTYPE html>
<html lang="en">
<head>
<meta charset="utf-8">
<title>Moberly Swift Solutions, LLC — Business Card</title>
<link rel="stylesheet" href="https://fonts.googleapis.com/css2?family=Cinzel:wght@500&family=Crimson+Pro:wght@400&family=Roboto+Condensed:wght@400&display=swap">
<style>
  :root {
    --page-bg: #e9e7e3;
    --card-white: #ffffff;
    --card-white-shade: #eceef0;
    --blue-light: #1f86cf;
    --blue-dark: #0e5aa3;
    --accent-green: #12907a;
    --brand-blue: #1a5f9e;
    --mark-fill: #2d7fb8;
    --ghost-mark: #c7d3e3;
    --text-light: #ffffff;
  }
  html, body {
    margin: 0;
    padding: 0;
    width: 1200px;
    height: 1200px;
    overflow: hidden;
    background: var(--page-bg);
  }
  .business-card {
    position: absolute;
    left: 75px;
    top: 300px;
    width: 1050px;
    height: 600px;
    background: linear-gradient(135deg, var(--card-white) 40%, var(--card-white-shade) 100%);
    box-shadow: 0 14px 36px rgba(0, 0, 0, 0.22);
    overflow: hidden;
  }
  .card-art {
    position: absolute;
    inset: 0;
  }
  .brand-lockup {
    position: absolute;
    left: 60px;
    top: 188px;
    display: flex;
    align-items: center;
    gap: 22px;
  }
  .brand-dot {
    width: 112px;
    height: 112px;
    border-radius: 50%;
    background: var(--mark-fill);
    flex: none;
  }
  .brand-rule {
    width: 4px;
    height: 136px;
    background: var(--accent-green);
    flex: none;
  }
  .brand-name {
    margin: 0;
    font-family: "Cinzel", serif;
    font-weight: 500;
    font-size: 30px;
    line-height: 40px;
    letter-spacing: 0.5px;
    color: var(--brand-blue);
  }
  .holder {
    position: absolute;
    right: 60px;
    top: 62px;
    text-align: right;
    color: var(--text-light);
    font-family: "Crimson Pro", serif;
  }
  .holder-name {
    margin: 0;
    font-size: 50px;
    font-weight: 400;
    line-height: 1.1;
    letter-spacing: 0.5px;
  }
  .holder-title {
    margin: 4px 0 0;
    font-size: 32px;
    line-height: 1.1;
  }
  .contact-list {
    position: absolute;
    left: 540px;
    top: 372px;
    margin: 0;
    padding: 0;
    list-style: none;
    font-family: "Roboto Condensed", sans-serif;
    font-size: 26px;
    color: var(--text-light);
  }
  .contact-item {
    display: flex;
    align-items: center;
    gap: 14px;
    height: 54px;
  }
  .contact-icon {
    width: 24px;
    height: 24px;
    flex: none;
  }
</style>
</head>
<body>
  <article class="business-card" aria-label="Business card for Lucia Pembrook, Moberly Swift Solutions, LLC">
    <svg class="card-art" width="1050" height="600" viewBox="0 0 1050 600" aria-hidden="true">
      <defs>
        <linearGradient id="panel-gradient" x1="0" y1="0" x2="0.3" y2="1">
          <stop offset="0" stop-color="var(--blue-light)"/>
          <stop offset="1" stop-color="var(--blue-dark)"/>
        </linearGradient>
      </defs>
      <circle class="ghost-circle" cx="190" cy="490" r="92" fill="none" stroke="var(--ghost-mark)" stroke-width="22" opacity="0.7"/>
      <polygon class="accent-stripe" points="590,0 600,0 440,600 430,600" fill="var(--accent-green)"/>
      <polygon class="blue-panel" points="610,0 1050,0 1050,600 450,600" fill="url(#panel-gradient)"/>
    </svg>

    <div class="brand-lockup">
      <div class="brand-dot"></div>
      <div class="brand-rule"></div>
      <p class="brand-name">MOBERLY SWIFT<br>SOLUTIONS<br>LLC</p>
    </div>

    <div class="holder">
      <h1 class="holder-name">Lucia Pembrook</h1>
      <p class="holder-title">President</p>
    </div>

    <ul class="contact-list">
      <li class="contact-item">
        <svg class="contact-icon" viewBox="0 0 24 24" aria-hidden="true"><path fill="currentColor" d="M6.6 10.8c1.4 2.8 3.8 5.1 6.6 6.6l2.2-2.2c.3-.3.7-.4 1-.2 1.1.4 2.3.6 3.6.6.6 0 1 .4 1 1V20c0 .6-.4 1-1 1C10.6 21 3 13.4 3 4c0-.6.4-1 1-1h3.5c.6 0 1 .4 1 1 0 1.3.2 2.5.6 3.6.1.3 0 .7-.2 1z"/></svg>
        <span>703-482-1947</span>
      </li>
      <li class="contact-item">
        <svg class="contact-icon" viewBox="0 0 24 24" aria-hidden="true"><path fill="currentColor" d="M2 5h20v14H2z"/><path fill="none" stroke="var(--blue-dark)" stroke-width="1.6" d="M2.5 5.5 12 13l9.5-7.5"/></svg>
        <span>lpembrook@moberlyswiftsolutions.example</span>
      </li>
      <li class="contact-item">
        <svg class="contact-icon" viewBox="0 0 24 24" aria-hidden="true" fill="none" stroke="currentColor" stroke-width="1.6"><circle cx="12" cy="12" r="9.5"/><ellipse cx="12" cy="12" rx="4.2" ry="9.5"/><path d="M2.5 12h19M4 7h16M4 17h16"/></svg>
        <span>www.moberlyswiftsolutions.example</span>
      </li>
    </ul>
  </article>
</body>
</html>
```